Create a Graphic About YOURSELF and PixelHarbor

PixelHarbor would like you (designers) to create an awesome graphic to promote YOURSELF and your profile on PixelHarbor!

Your graphic should communicate your name, your services and should mention PixelHarbor.

The design should be perfect for sharing on Chatterly. Here's an example of what we'd like http://blog.pixelharbor-example.ca/article/333/pixelharbor-launches-3000-hire-me-social-design-contest

Once you submitted your design, we'd love you to share the design ('advertisement') and promote yourself and PixelHarbor to your friends and potential customers. So make your submissions great and get your friends to vote for your design by 'Liking' it on Chatterly!

Prizes:
$1500 - "PixelHarbor Community" prize awarded to the designer with the most Chatterly 'Likes'
5 x $50 for the next 5 'most liked' designs on Chatterly

$1000 - "Hire Me" prize awarded to the designer who receives the most client invites
5 x $50 for the next 5 'most invited' designers

In summary, this is a great opportunity for you to increase your exposure to PixelHarbor customers and win cash prizes. Show off your design skills and get hired by PixelHarbor customers from around the world!

Target Market(s)

Fans, friends and customers of YOU

Industry/Entity Type

Cash

Requirements
Must have
• 1) Include your PixelHarbor user name on the graphic so customers can find you in the PixelHarbor Designer Directory
2) Include the tagline "Hire Me on PixelHarbor.com!" in your graphic design.
3) Share your design's URL on our Chatterly wall at http://chatterly-example.com/pixelharbor and get your friends to 'like' your design.
Nice to have
• 1) Include a tagline that expresses your design approach/philosophy
2) Artwork dimensions: 403 x 403 px
3) You can submit more than 1 design!
Should not have
• You must own the copyright of any images you use including stock imagery.

```html
<!DOCTYPE html>
<html lang="en">
<head>
<meta charset="utf-8">
<title>Hire Korvan on PixelHarbor</title>
<link rel="stylesheet" href="https://fonts.googleapis.com/css2?family=Kalam:wght@400;700&family=Kaushan+Script&family=Tinos&display=swap">
<style>
  :root {
    --bg-light: #fffaf0;
    --bg-mid: #f9c27a;
    --bg-deep: #ee7f1e;
    --ink: #111111;
    --accent-red: #e3141b;
    --accent-purple: #9a2cc4;
    --bag-black: #0b0908;
    --bag-gold: #6b5312;
    --email-yellow: #f3e21c;
    --brand-ink: #1d2a33;
    --hand-skin: #e7b894;
    --sleeve: #2a2a2e;
  }
  html, body {
    margin: 0;
    padding: 0;
    width: 1197px;
    height: 1200px;
    overflow: hidden;
    background: var(--bg-light);
  }
  .poster {
    display: block;
    width: 1197px;
    height: 1200px;
  }
  .tagline {
    font-family: "Kalam", cursive;
    font-size: 122px;
    fill: var(--ink);
  }
  .tagline .highlight, .tagline.highlight { fill: var(--accent-red); }
  .hire-call {
    font-family: "Kalam", cursive;
    font-size: 92px;
    font-weight: 700;
    fill: var(--accent-purple);
  }
  .designer-name {
    font-family: "Kaushan Script", cursive;
    font-size: 150px;
    fill: var(--accent-red);
  }
  .designer-email {
    font-family: "Tinos", serif;
    font-size: 48px;
    fill: var(--email-yellow);
  }
  .brand-name {
    font-family: "Kalam", cursive;
    font-size: 84px;
    font-weight: 700;
    fill: var(--brand-ink);
  }
</style>
</head>
<body>
<svg class="poster" viewBox="0 0 1197 1200" xmlns="http://www.w3.org/2000/svg">
  <defs>
    <linearGradient id="backdrop" x1="0" y1="0" x2="1" y2="0.25">
      <stop offset="0" stop-color="var(--bg-light)"/>
      <stop offset="0.45" stop-color="var(--bg-mid)"/>
      <stop offset="1" stop-color="var(--bg-deep)"/>
    </linearGradient>
    <radialGradient id="glow" cx="0.1" cy="0.35" r="0.7">
      <stop offset="0" stop-color="#ffffff" stop-opacity="0.85"/>
      <stop offset="1" stop-color="#ffffff" stop-opacity="0"/>
    </radialGradient>
    <linearGradient id="hand-tones" x1="0" y1="0" x2="0" y2="1">
      <stop offset="0" stop-color="var(--sleeve)"/>
      <stop offset="0.22" stop-color="var(--hand-skin)"/>
      <stop offset="1" stop-color="#c9a23a" stop-opacity="0.6"/>
    </linearGradient>
    <radialGradient id="bag-tones" cx="0.55" cy="0.3" r="0.75">
      <stop offset="0" stop-color="var(--bag-gold)"/>
      <stop offset="0.6" stop-color="var(--bag-black)"/>
    </radialGradient>
  </defs>

  <rect class="backdrop" width="1197" height="1200" fill="url(#backdrop)"/>
  <rect class="backdrop-glow" width="1197" height="1200" fill="url(#glow)"/>

  <rect class="hand-art" x="190" y="0" width="250" height="425" rx="30"
        fill="url(#hand-tones)" role="img"
        aria-label="A hand in a dark suit sleeve holding the gold handles of a shopping bag"/>

  <rect class="bag-art" x="6" y="420" width="630" height="775"
        fill="url(#bag-tones)" role="img"
        aria-label="Black shopping bag decorated with a golden holly and bauble ornament"/>

  <text class="designer-name" x="84" y="1078" textLength="448" lengthAdjust="spacingAndGlyphs">Korvan</text>
  <text class="designer-email" x="28" y="1170" textLength="593" lengthAdjust="spacingAndGlyphs">korvangfx@example.com</text>

  <g class="tagline-block">
    <text class="tagline" x="965" y="168" textLength="197" lengthAdjust="spacingAndGlyphs">For</text>
    <text class="tagline" x="680" y="322" textLength="453" lengthAdjust="spacingAndGlyphs">Quality</text>
    <text class="tagline" x="526" y="504" textLength="593" lengthAdjust="spacingAndGlyphs"><tspan class="highlight">Per</tspan>fection,</text>
    <text class="tagline highlight" x="655" y="600">&amp;</text>
    <text class="tagline" x="526" y="742" textLength="570" lengthAdjust="spacingAndGlyphs"><tspan class="highlight">Ex</tspan>perience</text>
  </g>

  <g class="hire-block">
    <text class="hire-call" x="713" y="938" textLength="257" lengthAdjust="spacingAndGlyphs">Hire me</text>
    <text class="hire-call" x="834" y="1040" textLength="130" lengthAdjust="spacingAndGlyphs">on</text>
  </g>

  <text class="brand-name" x="680" y="1158" textLength="480" lengthAdjust="spacingAndGlyphs">PixelHarbor</text>
</svg>
</body>
</html>
```